Feral Tundra, a 3d voxel survival video game needs a card for gaming conventions

I am the lead developer for Feral Tundra http://www.FeralTundra.example and need a business card to hand out at an indie gaming convention
The card would need to include the game name, website url, my name, position (Lead Developer), e-mail and phone number
The game is a 3d, voxel (with smooth terrain) based survival game with guns and wildlife. The main icon of the game would likely be a grizzly bear but I am willing to accept other designs too.
Attached is a media kit for the game with some images you can use but don't have to its just what little art I can provide. Anything on the website or from the video game can also be used. unrelated art can also be used.
Target Market(s)
Indie Developers/publishers at conferences
Industry/Entity Type
Games
Contact Information for Business Card
Name: Corin Wexford
Position: Lead Developer
E-mail: Gray_Lanterns@mailnest.example
Phone number: 555-372-9186
Look and feel

```html
<!DOCTYPE html>
<html lang="en">
<head>
<meta charset="utf-8">
<title>Feral Tundra – Business Card</title>
<link rel="stylesheet" href="https://fonts.googleapis.com/css2?family=Open+Sans:wght@400;600;700;800&display=swap">
<style>
  :root {
    --page-bg: #d9d6cf;
    --front-top: #f1f1ef;
    --front-bottom: #d8d9d6;
    --mist: #cfd0cc;
    --fur-light: #a9744a;
    --fur-dark: #6b4126;
    --rock: #e4e2dc;
    --ink: #1f1f1f;
    --ink-soft: #3a3a3a;
    --brand-red: #b8322a;
    --back-center: #ece8d2;
    --back-mid: #7d7a4c;
    --back-edge: #24230f;
    --icon: #222;
  }
  * { box-sizing: border-box; margin: 0; padding: 0; }
  html, body { width: 1200px; height: 780px; overflow: hidden; }
  body {
    background: var(--page-bg);
    font-family: "Open Sans", Arial, sans-serif;
    position: relative;
  }
  .card {
    position: absolute;
    top: 235px;
    width: 540px;
    height: 309px;
    overflow: hidden;
    box-shadow: 0 6px 18px rgba(0,0,0,0.25);
  }
  .card--front {
    left: 40px;
    background: linear-gradient(180deg, var(--front-top) 0%, var(--mist) 55%, var(--front-bottom) 100%);
  }
  .card--back {
    left: 620px;
    background: radial-gradient(ellipse at 50% 50%, var(--back-center) 0%, var(--back-mid) 50%, var(--back-edge) 100%);
  }
  .bear-photo {
    position: absolute;
    left: 20px;
    top: 40px;
    width: 250px;
    height: 269px;
    background:
      radial-gradient(ellipse 100px 95px at 120px 120px, var(--fur-light) 0%, var(--fur-dark) 75%, transparent 100%),
      linear-gradient(180deg, transparent 0%, transparent 80%, var(--rock) 80%, var(--rock) 100%);
  }
  .front-info {
    position: absolute;
    left: 300px;
    top: 62px;
    color: var(--ink);
  }
  .brand-name {
    font-weight: 800;
    font-size: 23px;
    letter-spacing: 1px;
    text-transform: uppercase;
    color: var(--brand-red);
    margin-bottom: 12px;
  }
  .person-name {
    font-weight: 600;
    font-size: 19px;
    line-height: 1.1;
  }
  .person-role {
    font-size: 13px;
    color: var(--ink-soft);
    margin-bottom: 12px;
  }
  .contact-list { list-style: none; }
  .contact-item {
    display: flex;
    align-items: center;
    gap: 7px;
    font-size: 12px;
    line-height: 1.75;
    color: var(--ink);
  }
  .contact-icon { width: 12px; height: 12px; flex: none; }
  .bear-head {
    position: absolute;
    left: 305px;
    top: 58px;
    width: 145px;
    height: 92px;
    border-radius: 50%;
    background: radial-gradient(ellipse at 50% 50%, var(--fur-light) 0%, var(--fur-dark) 60%, transparent 100%);
  }
  .back-brand {
    position: absolute;
    font-weight: 800;
    font-size: 58px;
    letter-spacing: 4px;
    text-transform: uppercase;
    color: var(--brand-red);
    line-height: 1;
  }
  .back-brand--first { left: 90px; top: 88px; }
  .back-brand--second { left: 135px; top: 160px; }
</style>
</head>
<body>
  <section class="card card--front">
    <div class="bear-photo" role="img" aria-label="Photo of a brown grizzly bear standing on a pale rock in misty forest"></div>
    <div class="front-info">
      <p class="brand-name">Feral Tundra</p>
      <p class="person-name">Corin Wexford</p>
      <p class="person-role">Lead Developer</p>
      <ul class="contact-list">
        <li class="contact-item">
          <svg class="contact-icon" viewBox="0 0 12 12"><rect width="12" height="12" rx="1.5" fill="var(--icon)"/><path d="M3.5 2.8c.4-.3.8-.2 1 .2l.6 1.1c.2.4.1.7-.2 1l-.4.3c.4.8 1 1.4 1.8 1.8l.3-.4c.3-.3.6-.4 1-.2l1.1.6c.4.2.5.6.2 1-.8 1-1.8 1.1-3.2.2C4.4 7.6 3.6 6.7 3 5.5c-.6-1.3-.4-2.1.5-2.7z" fill="#fff"/></svg>
          <span>555-372-9186</span>
        </li>
        <li class="contact-item">
          <svg class="contact-icon" viewBox="0 0 12 12"><rect width="12" height="12" rx="1.5" fill="var(--icon)"/><rect x="2.5" y="3.5" width="7" height="5" fill="none" stroke="#fff" stroke-width="1"/><path d="M2.5 3.5 6 6.3 9.5 3.5" fill="none" stroke="#fff" stroke-width="1"/></svg>
          <span>Gray_Lanterns@mailnest.example</span>
        </li>
        <li class="contact-item">
          <svg class="contact-icon" viewBox="0 0 12 12"><circle cx="6" cy="6" r="6" fill="var(--icon)"/><circle cx="6" cy="6" r="3.6" fill="none" stroke="#fff" stroke-width=".9"/><path d="M2.4 6h7.2M6 2.4c-1.5 2-1.5 5.2 0 7.2M6 2.4c1.5 2 1.5 5.2 0 7.2" fill="none" stroke="#fff" stroke-width=".8"/></svg>
          <span>www.feraltundra.example</span>
        </li>
      </ul>
    </div>
  </section>

  <section class="card card--back">
    <div class="bear-head" role="img" aria-label="Roaring grizzly bear head illustration"></div>
    <p class="back-brand back-brand--first">Feral</p>
    <p class="back-brand back-brand--second">Tundra</p>
  </section>
</body>
</html>
```